Brenwick Structures Construction Company Seeking Modern Website

We are a small construction company wanting to create a web presence. We don't have much in the way of current content but will get photos as they come in. Attached is a picture of our business card.
The pages we would like on the menu are:
Home
Portfolio
Product Specs
Testimonials
Our Process
Contact
Some designs we like are:
http://www.tovandrafters.example/
http://www.qrkframes.example/
http://harnestshed.example/
http://pellowbarns.example/
Not much requirements other than that so feel free to be creative!
Target Market(s)
Construction
Commercial and Residential Buildings
Industry/Entity Type
Construction Company
Number of Pages Required
5+ page

```html
<!DOCTYPE html>
<html lang="en">
<head>
<meta charset="utf-8">
<title>Brenwick Structures – Building Construction</title>
<link href="https://fonts.googleapis.com/css2?family=Dosis:wght@300;400;500;600&display=swap" rel="stylesheet">
<style>
:root{
  --navy:#34487a;
  --navy-dark:#26355a;
  --navy-deep:#2c3d66;
  --band:#3a5084;
  --white:#ffffff;
  --ink:#333a48;
  --muted:#6b7388;
  --accent:#2aa9e0;
  --btn:#2f4272;
  --grey-tab:#d9dde5;
  --caption:#5a6f9d;
  --date:#e8d545;
}
*{margin:0;padding:0;box-sizing:border-box}
html,body{width:1200px;height:2535px;overflow:hidden}
body{font-family:"Dosis",sans-serif;color:var(--ink);background:var(--white);position:relative}
.abs{position:absolute}
.topbar{left:0;top:0;width:1200px;height:45px;background:var(--navy-dark);color:var(--white);font-size:13px}
.topbar .contact{left:113px;top:14px;display:flex;gap:22px;align-items:center}
.topbar .contact span{display:flex;align-items:center;gap:6px}
.socials{display:flex;gap:8px}
.socials i{width:26px;height:26px;border-radius:50%;background:var(--white);display:block}
.topbar .socials{right:113px;top:10px}
.header{left:0;top:45px;width:1200px;height:144px;background:var(--navy)}
.brand{left:0;width:1200px;top:14px;text-align:center;font-size:42px;font-weight:600;color:var(--accent);line-height:1}
.tagline{left:0;width:1200px;top:64px;text-align:center;font-size:15px;color:var(--accent)}
.nav{left:172px;top:100px;width:856px;height:44px;border:2px solid var(--white);display:flex;background:var(--navy-dark)}
.nav a{flex:1;color:var(--white);font-size:17px;display:flex;align-items:center;justify-content:center;letter-spacing:.5px}
.nav a.active{background:var(--grey-tab);color:var(--ink);border:4px solid var(--navy-dark)}
.hero{left:0;top:189px;width:1200px;height:473px;background:linear-gradient(180deg,#b9c8d8 0%,#d7d9d2 35%,#9a9780 62%,#5c7a3a 85%,#4a6a2c 100%)}
.hero-line{left:100px;background:rgba(20,24,32,.6);color:var(--white);font-size:26px;padding:4px 14px;letter-spacing:1px}
.welcome-title{left:0;width:1200px;top:684px;font-size:30px;font-weight:400;color:var(--navy);text-align:center}
.welcome-title b{color:var(--accent);font-weight:400}
.welcome-text{left:300px;width:600px;top:734px;font-size:14px;text-align:center;line-height:1.4}
.btn{background:var(--btn);color:var(--white);font-size:14px;display:flex;align-items:center;justify-content:center}
.welcome-btn{left:544px;top:792px;width:106px;height:30px}
.tabs{left:113px;top:842px;display:flex;gap:10px}
.tabs span{height:31px;padding:0 22px;display:flex;align-items:center;font-size:14px;background:var(--navy);color:var(--white)}
.tabs span.active{background:var(--navy-dark)}
.carousel{left:0;top:873px;width:1200px;height:268px;background:var(--band)}
.card{width:225px}
.card .photo{height:157px}
.card .cap{height:31px;background:var(--caption);color:var(--white);font-size:14px;display:flex;align-items:center;justify-content:center}
.arrow{width:40px;height:40px;border-radius:50%;border:2px solid var(--white);display:flex;align-items:center;justify-content:center}
.process-photo{left:113px;top:1189px;width:312px;height:242px;background:linear-gradient(180deg,#c7b9a0,#8d7a5e 60%,#6b5f4a)}
.process-title{left:448px;top:1184px;font-size:30px;font-weight:400;color:var(--navy)}
.process-title b{color:var(--accent);font-weight:400}
.process-text{left:448px;top:1228px;width:640px;font-size:12px;line-height:1.4}
.process-text p{margin-bottom:10px}
.process-btn{left:448px;top:1400px;width:110px;height:31px}
.projects{left:0;top:1456px;width:1200px;height:319px;background:var(--band);color:var(--white)}
.projects h2{position:absolute;left:0;width:1200px;top:14px;text-align:center;font-size:30px;font-weight:400}
.projects .intro{position:absolute;left:113px;width:975px;top:58px;font-size:12px;text-align:center;line-height:1.35}
.projects .card .photo{height:133px}
.col-title{font-size:32px;font-weight:400;color:var(--navy)}
.col-title b{color:var(--accent);font-weight:400}
.blog-item{display:flex;gap:17px}
.blog-item .photo{width:163px;height:121px;flex:none}
.blog-item h3{font-size:21px;font-weight:500;color:var(--navy);line-height:1.1}
.blog-item .meta{font-size:11.5px;color:var(--accent);margin:3px 0 6px}
.blog-item p{font-size:12px;line-height:1.35;width:270px}
.testi{display:flex;gap:16px}
.testi .photo{width:127px;height:113px;flex:none;background:linear-gradient(180deg,#d7d9de,#9ea5b3)}
.testi .quote{font-size:12px;line-height:1.4;color:var(--muted);width:270px}
.testi .name{font-size:16px;color:var(--ink);margin-top:8px}
.testi .role{font-size:12px;color:var(--muted)}
.qmark{font-size:44px;color:var(--ink);line-height:.9;font-weight:600}
.divider{height:1px;background:#c9ced8}
.footer{left:0;top:2149px;width:1200px;height:386px;background:var(--navy-deep);color:var(--white)}
.footer h4{font-size:15px;font-weight:500;margin-bottom:10px;letter-spacing:.5px}
.footer p{font-size:11.5px;line-height:1.35}
.footer .date{color:var(--date);margin:4px 0 8px}
.newsletter{display:flex}
.newsletter .field{width:230px;height:34px;background:var(--white);color:#999;font-size:12px;display:flex;align-items:center;padding-left:8px}
.newsletter .submit{width:70px;height:34px;background:var(--navy-dark);font-size:14px;display:flex;align-items:center;justify-content:center}
.copyright{left:113px;top:322px;width:975px;border-top:1px solid rgba(255,255,255,.4);text-align:center;font-size:12px;padding-top:16px}
</style>
</head>
<body>

<div class="abs topbar">
  <div class="abs contact">
    <span><svg width="14" height="14" viewBox="0 0 24 24"><path fill="#fff" d="M6.6 10.8a15 15 0 006.6 6.6l2.2-2.2a1 1 0 011-.25 11 11 0 003.6.6 1 1 0 011 1V20a1 1 0 01-1 1A17 17 0 013 4a1 1 0 011-1h3.5a1 1 0 011 1 11 11 0 00.6 3.6 1 1 0 01-.25 1z"/></svg>400 555 0148</span>
    <span><svg width="16" height="12" viewBox="0 0 16 12"><rect x="0.5" y="0.5" width="15" height="11" fill="none" stroke="#fff"/><path d="M1 1l7 6 7-6" fill="none" stroke="#fff"/></svg>brenwickstructures.example</span>
  </div>
  <div class="abs socials"><i></i><i></i><i></i></div>
</div>

<header class="abs header">
  <div class="abs brand">Brenwick Structures</div>
  <div class="abs tagline">Building Dreams So You Can Build Memories</div>
  <nav class="abs nav">
    <a class="active">HOME</a><a>PORTFOLIO</a><a>PRODUCT SPECS</a><a>TESTIMONIALS</a><a>OUR PROCESS</a><a>CONTACT</a>
  </nav>
</header>

<section class="abs hero" role="img" aria-label="Large beige post-frame building with wide garage doors on a grassy lot under a pale sky">
  <div class="abs hero-line" style="left:113px;top:185px">WE ARE OFFERING</div>
  <div class="abs hero-line" style="left:113px;top:252px">THE BEST REAL ESTATE DEALS</div>
</section>

<h1 class="abs welcome-title">WELCOME TO <b>BRENWICK</b> BUILDING CONSTRUCTION</h1>
<p class="abs welcome-text">Put Halvern Post Buildings' unique blend of Amish craftsmanship and professional design and management services to work on your project today. Superior quality at a price you will appreciate.</p>
<div class="abs btn welcome-btn">Read more</div>
<div class="abs tabs"><span class="active">RESIDENTIAL</span><span>COMMERCIAL</span><span>AGRICULTURAL</span></div>

<section class="abs carousel">
  <div class="abs arrow" style="left:56px;top:110px"><svg width="20" height="20" viewBox="0 0 20 20"><path d="M13 4l-6 6 6 6" fill="none" stroke="#fff" stroke-width="2.5"/></svg></div>
  <div class="abs arrow" style="left:1104px;top:110px"><svg width="20" height="20" viewBox="0 0 20 20"><path d="M7 4l6 6-6 6" fill="none" stroke="#fff" stroke-width="2.5"/></svg></div>
  <div class="abs card" style="left:113px;top:54px"><div class="photo" role="img" aria-label="Red barn-style post building with white trim" style="background:linear-gradient(180deg,#c9d6e6,#a33b3b 55%,#6f8a4a)"></div><div class="cap">Put Halvern Post Building</div></div>
  <div class="abs card" style="left:363px;top:54px"><div class="photo" role="img" aria-label="Red post building with two garage doors" style="background:linear-gradient(180deg,#d0dbe8,#9e3434 50%,#7e8a68)"></div><div class="cap">Put Halvern Post Building</div></div>
  <div class="abs card" style="left:612px;top:54px"><div class="photo" role="img" aria-label="Red garage building with white doors" style="background:linear-gradient(180deg,#c2cfdf,#a83535 45%,#8a8f80)"></div><div class="cap">Put Halvern Post Building</div></div>
  <div class="abs card" style="left:862px;top:54px"><div class="photo" role="img" aria-label="Red gambrel barn on open lawn" style="background:linear-gradient(180deg,#bcd0e6,#b03a3a 55%,#6d9444)"></div><div class="cap">Put Halvern Post Building</div></div>
</section>

<div class="abs process-photo" role="img" aria-label="Wooden post frame under construction with trusses on site"></div>
<h2 class="abs process-title"><b>OUR MANUFACTURING</b> PROCESS</h2>
<div class="abs process-text">
  <p>Put Halvern Post Buildings' unique blend of Amish craftsmanship and professional design and management services to work on your project today. Superior quality at a price you will appreciate.</p>
  <p>Put Halvern Post Buildings' unique blend of Amish craftsmanship and professional design and management services to work on your project today. Superior quality at a price you will appreciate. Put Halvern Post Buildings' unique blend of Amish craftsmanship and professional design and management services to work on your project today. Superior quality at a price you will appreciate.</p>
  <p>Put Halvern Post Buildings' unique blend of Amish craftsmanship and professional design and management services to work on your project today. Superior quality at a price you will appreciate. Put Halvern Post Buildings' unique blend of Amish craftsmanship and professional design and management services to work on your project today. Superior quality at a price you will appreciate.</p>
</div>
<div class="abs btn process-btn">Read more</div>

<section class="abs projects">
  <h2>UPCOMING PROJECTS</h2>
  <p class="intro">Put Halvern Post Buildings' unique blend of Amish craftsmanship and professional design and management services to work on your project today. Superior quality at a price you will appreciate. Put Halvern Post Buildings' unique blend of Amish craftsmanship and professional design and management services to work on your project today. Superior quality at a price you will appreciate.</p>
  <div class="abs card" style="left:113px;top:110px"><div class="photo" role="img" aria-label="Timber frame skeleton of a building in progress" style="background:linear-gradient(180deg,#a9c3de,#b49a74 60%,#7a8a55)"></div><div class="cap">Put Halvern Post Building</div></div>
  <div class="abs card" style="left:363px;top:110px"><div class="photo" role="img" aria-label="Wooden roof trusses being set on posts" style="background:linear-gradient(180deg,#c8d6e5,#b89f7a 55%,#8d7f62)"></div><div class="cap">Put Halvern Post Building</div></div>
  <div class="abs card" style="left:612px;top:110px"><div class="photo" role="img" aria-label="Post frame building shell among green trees" style="background:linear-gradient(180deg,#9fb8d2,#5f8a3c 55%,#4d6f2e)"></div><div class="cap">Put Halvern Post Building</div></div>
  <div class="abs card" style="left:862px;top:110px"><div class="photo" role="img" aria-label="Large framed structure with exposed wooden studs" style="background:linear-gradient(180deg,#c5d3e3,#bfa37c 55%,#8f8a6a)"></div><div class="cap">Put Halvern Post Building</div></div>
</section>

<h2 class="abs col-title" style="left:113px;top:1796px">LATEST <b>BLOG</b></h2>
<div class="abs blog-item" style="left:113px;top:1851px">
  <div class="photo" role="img" aria-label="Red post building with white garage doors" style="background:linear-gradient(180deg,#c6d5e6,#a23838 55%,#7f9a58)"></div>
  <div><h3>Put Halvern Post Building</h3><div class="meta">16 Minutes Ago / 1 Comments</div><p>Put Halvern Post Buildings' unique blend of Amish craftsmanship and professional design and management services to work on your project today. Superior quality at a price.</p></div>
</div>
<div class="abs blog-item" style="left:113px;top:1990px">
  <div class="photo" role="img" aria-label="Grey post building with large doors" style="background:linear-gradient(180deg,#cfd8e3,#8d9299 55%,#7c8f5c)"></div>
  <div><h3>Put Halvern Post Building</h3><div class="meta">16 Minutes Ago / 1 Comments</div><p>Put Halvern Post Buildings' unique blend of Amish craftsmanship and professional design and management services to work on your project today. Superior quality at a price.</p></div>
</div>

<h2 class="abs col-title" style="left:611px;top:1796px"><b>TESTI</b>MONIALS</h2>
<div class="abs testi" style="left:611px;top:1851px">
  <div class="photo" role="img" aria-label="Portrait of client Jared Snell"></div>
  <div style="display:flex;gap:8px">
    <div class="qmark">“</div>
    <div><p class="quote">Our new shop went up on time and on budget. The crew was tidy, friendly and answered every question we asked along the way.</p>
    <div class="name">Jared Snell</div><div class="role">( Doctor )</div></div>
    <div class="qmark" style="align-self:flex-end">”</div>
  </div>
</div>
<div class="abs divider" style="left:611px;top:1986px;width:477px"></div>
<div class="abs testi" style="left:611px;top:2003px">
  <div class="photo" role="img" aria-label="Portrait of client Alden Cray"></div>
  <div style="display:flex;gap:8px">
    <div class="qmark">“</div>
    <div><p class="quote">Solid work from the first drawing to the final bolt. Our barn looks great and we would gladly hire this team again soon.</p>
    <div class="name">Alden Cray</div><div class="role">( Doctor )</div></div>
    <div class="qmark" style="align-self:flex-end">”</div>
  </div>
</div>

<footer class="abs footer">
  <div class="abs" style="left:113px;top:28px;width:300px">
    <h4>ABOUT US</h4>
    <p>Sturdy frames, honest pricing and careful crews. We plan each building with you and stay on site until the last panel is fixed.</p>
    <p style="margin-top:10px">From small garages to wide farm sheds, our team brings decades of skill to every job. Call us to talk about your plans and get a fair quote for your next project.</p>
    <div class="btn" style="width:82px;height:28px;margin-top:22px;background:var(--navy-dark)">Read more</div>
    <div class="newsletter" style="margin-top:18px"><div class="field">News Letter</div><div class="submit">SUBMIT</div></div>
  </div>
  <div class="abs" style="left:448px;top:28px;width:290px">
    <h4>LATEST TWEET</h4>
    <p>New roof trusses arrived today for the hillside barn project. Framing starts Monday, weather permitting, so stay tuned for photos.</p>
    <p class="date">Posted on 12th August 2014</p>
    <p>Thanks to every family who visited our open yard day. Your kind words keep our crews working hard each week.</p>
    <p class="date">Posted on 12th August 2014</p>
    <p>Two more storage buildings finished this week and handed over.</p>
    <p class="date">Posted on 12th August 2014</p>
  </div>
  <div class="abs" style="left:778px;top:28px;width:300px">
    <h4>CONTACT INFO</h4>
    <p style="font-size:14px;margin-bottom:4px">NEW YORK</p>
    <p>Ostrel Timberworks Office<br>18 Carrow Lane, 10450 New York<br>Tel 400-555-0172</p>
    <p style="margin-top:16px">Ostrel Timberworks Yard<br>42 Marden Road, 10450 New York<br>Tel 400-555-0186</p>
    <div class="socials" style="margin-top:34px"><i></i><i></i><i></i></div>
  </div>
  <div class="abs copyright">© 2015 Brenwick Structures. All Rights Reserved.</div>
</footer>

</body>
</html>
```